Meridale Holding Partners Corporate Showcase

Provide an attractive Corporate Website for a boutique Investment Company to showcase our activities and corporate interests.

Our Company works across a number of Sectors including

Real Estate
E-Commerce
Healthcare
Beauty & Personal Care
Technology
Resources

Lets keep the personality

Modern
Global
Sophisticated
Calm
Interesting

Lets keep the pages with MINIMAL Words
Lets use Photos/ Imagery to tell the story

We'll need a Banner Menu -
About Us
Expertise
Global Outlook
Sectors
Management
Media
Contact Us

Many thanks
Best wishes
Derek.

Target Market(s)

Investors
Clients

Coding

Coded - Design and coding required

Number of Pages Required

5+ page

Font styles to use
Sans Serif

Colors
886aae
3176b5
00a990
f68e4d
f04a50
e667a6

Requirements
Must have
• WordPress Coding

Checkout this Website for look and feel - its cool:
www.kvr.com

Meridale Holding Stewardship
(Meridale Holding Partners LLP)
London
E4 2RL
United Kingdom

www.MeridaleHoldingStewardship.com
Nice to have
• Sophisticated colour palette - black/ brown/ blue/ purple/

```html
<!DOCTYPE html>
<html lang="en">
<head>
<meta charset="utf-8">
<title>Meridale Holding Partners</title>
<link rel="stylesheet" href="https://fonts.googleapis.com/css2?family=Outfit:wght@300;500;600;700&family=Nunito+Sans:wght@400;600;700&display=swap">
<style>
:root{
  --purple:#886aae;
  --purple-dark:#6f548f;
  --ink:#141414;
  --text:#555;
  --muted:#8a8a8a;
  --grey-bg:#f1f1f3;
  --black:#0b0b0b;
  --white:#fff;
  --navy:#0a0f3a;
}
*{box-sizing:border-box;margin:0;padding:0}
html,body{width:1200px;height:5025px;overflow:hidden}
body{position:relative;font-family:"Nunito Sans",sans-serif;color:var(--text);background:var(--white)}
.abs{position:absolute}
h1,h2,h3,h4,.brand,.btn,.tag{font-family:"Outfit",sans-serif}
.section-title{font-size:44px;font-weight:600;color:var(--ink);text-align:center}
.section-title::after{content:"";display:block;width:44px;height:5px;background:var(--purple);margin:14px auto 0;border-radius:3px}
.left-title{font-size:44px;font-weight:600;color:var(--ink)}
.left-title::after{content:"";display:block;width:44px;height:5px;background:var(--purple);margin-top:14px;border-radius:3px}
.btn{display:inline-flex;align-items:center;justify-content:center;background:var(--purple);color:var(--white);font-weight:600;font-size:16px;border-radius:30px;height:48px;padding:0 44px}
.more{font-family:"Outfit",sans-serif;color:var(--purple);font-weight:500;font-size:16px;display:flex;align-items:center;gap:10px}
.photo{display:block}

/* top bar & nav */
.topbar{left:0;top:0;width:1200px;height:39px;background:var(--purple);color:var(--white);font-family:"Outfit",sans-serif;font-weight:500;font-size:15px;display:flex;justify-content:flex-end;align-items:center;gap:46px;padding-right:90px}
.topbar span{display:flex;align-items:center;gap:8px}
.nav{left:0;top:39px;width:1200px;height:84px;background:var(--white);box-shadow:0 2px 6px rgba(0,0,0,.06)}
.brand{color:var(--purple);font-weight:600;font-size:20px;letter-spacing:2px;line-height:1.05;text-transform:uppercase}
.nav .brand{left:90px;top:20px}
.menu{left:351px;top:31px;width:760px;display:flex;justify-content:space-between;font-size:15px;color:#333;font-family:"Outfit",sans-serif;font-weight:300}
.menu .active{color:var(--purple);font-weight:600;border-bottom:2px solid var(--purple);padding-bottom:3px}

/* hero */
.hero{left:0;top:123px;width:1200px;height:591px;background:radial-gradient(ellipse at 15% 75%,#b33a8a 0%,#4a2a8a 22%,transparent 50%),radial-gradient(ellipse at 75% 25%,#1e3c9a 0%,transparent 45%),linear-gradient(180deg,#0c1350,#070a30)}
.hero-copy{left:0;top:240px;width:1200px;text-align:center;color:var(--white)}
.hero-copy h1{font-size:50px;font-weight:700;letter-spacing:2px;text-transform:uppercase;line-height:1}
.hero-copy p{font-family:"Outfit",sans-serif;font-weight:300;font-size:36px;letter-spacing:1px;margin-top:4px}

/* about */
.about-text{left:92px;top:842px;width:470px}
.about-text p{font-size:15px;line-height:27px;margin-top:28px}
.about-text p + p{margin-top:26px}
.about-text .btn{margin-top:34px}

/* sectors */
.sectors{left:0;top:1325px;width:1200px;height:1194px;background:var(--grey-bg)}
.card{width:328px;height:441px;background:var(--white)}
.card .photo{width:328px;height:234px}
.card .tag{position:absolute;left:27px;top:207px;width:274px;height:52px;background:var(--purple);color:var(--white);font-weight:600;font-size:16px;display:flex;align-items:center;justify-content:center}
.card p{position:absolute;left:20px;top:290px;width:288px;text-align:center;font-size:14.5px;line-height:27px;color:var(--muted)}
.card .more{position:absolute;left:0;top:392px;width:328px;justify-content:center;font-size:14px;font-weight:600}

/* outlook */
.outlook-text{left:626px;top:2612px;width:484px}
.outlook-text p{font-size:14.5px;line-height:31px;text-align:justify;margin-top:22px}
.outlook-text .btn{margin-top:28px}

/* media */
.post{background:var(--white);box-shadow:0 4px 14px rgba(0,0,0,.12)}
.post h3{font-size:21px;font-weight:600;color:var(--ink);line-height:30px}
.post p{font-size:13px;line-height:26px;color:var(--muted)}
.mini{width:487px;height:186px}
.mini .body{position:absolute;top:18px;width:300px}
.mini h3{font-size:18px;line-height:26px}
.mini p{margin-top:6px;font-size:12.5px;line-height:25px}
.mini .more{margin-top:10px;font-size:15px}
.mini .photo{position:absolute;top:0;width:156px;height:186px}

/* contact */
.footer-bg{left:0;top:4298px;width:1200px;height:727px;background:var(--black)}
.contact{left:90px;top:3996px;width:1020px;height:612px;background:var(--purple)}
.contact .section-title{color:var(--white);margin-top:64px}
.contact .section-title::after{background:var(--white)}
.field{position:absolute;background:var(--white);font-size:13px;color:#aaa;display:flex;align-items:center;gap:8px;padding-left:16px}
.field.area{align-items:flex-start;padding-top:16px}
.submit{left:419px;top:492px;width:182px;height:48px;border:2px solid var(--white);border-radius:30px;color:var(--white);font-family:"Outfit",sans-serif;font-weight:600;font-size:16px;display:flex;align-items:center;justify-content:center}

/* footer */
.foot-brand{left:90px;top:4692px;color:var(--white)}
.socials{left:90px;top:4775px;display:flex;gap:24px}
.socials span{width:16px;height:16px;background:var(--white);border-radius:3px}
.foot-h{font-size:20px;font-weight:600;color:var(--white)}
.foot-h::after{content:"";display:block;width:16px;height:2px;background:var(--purple);margin-top:12px}
.foot-list{list-style:none;color:var(--white);font-size:14px;line-height:30.5px}
.copy{left:0;top:4978px;width:1200px;text-align:center;color:var(--white);font-size:12px}
</style>
</head>
<body>

<header>
  <div class="abs topbar">
    <span><svg width="16" height="12" viewBox="0 0 16 12"><rect x="0.5" y="0.5" width="15" height="11" rx="1" fill="none" stroke="#fff"/><path d="M1 1l7 6 7-6" fill="none" stroke="#fff"/></svg>hello@meridaleholding.example</span>
    <span><svg width="14" height="14" viewBox="0 0 14 14"><path d="M3 1l2.5 3-1.5 1.5c1 2 2.5 3.5 4.5 4.5L10 8.5l3 2.5-1.5 2C6 13 1 8 1 2.5z" fill="#fff"/></svg>+0 000 555 0142</span>
  </div>
  <nav class="abs nav">
    <div class="abs brand">Meridale Holding<br>Partners</div>
    <div class="abs menu">
      <span class="active">Home</span><span>About Us</span><span>Expertise</span><span>Global Outlook</span><span>Sectors</span><span>Management</span><span>Media</span><span>Contact Us</span>
    </div>
  </nav>
</header>

<section class="abs hero" role="img" aria-label="Abstract wave of glowing dots in magenta and blue on a dark navy field"></section>
<div class="abs hero-copy">
  <h1>Meridale Holding Partners</h1>
  <p>Growing the Next Generation of Business</p>
</div>

<!-- about -->
<div class="abs" style="left:913px;top:714px;width:287px;height:611px;background:var(--purple)"></div>
<div class="abs photo" role="img" aria-label="Businessman overlooking a city skyline at dusk with a glowing world map overlay" style="left:624px;top:798px;width:576px;height:443px;background:linear-gradient(180deg,#8f9bd6 0%,#6a76b8 45%,#3b4a7e 75%,#1e2748 100%)"></div>
<div class="abs about-text">
  <h2 class="left-title">About Us</h2>
  <p>Lorem ipsum dolor sit amet, consectetur adipiscing elit, sed do eiusmod tempor incididunt ut labore et dolore magna aliqua. Ut enim ad minim veniam, quis nostrud exercitation</p>
  <p>Duis aute irure dolor in reprehenderit in voluptate velit esse cillum dolore eu fugiat nulla pariatur.</p>
  <span class="btn">Read More</span>
</div>

<!-- sectors -->
<section class="abs sectors">
  <h2 class="abs section-title" style="left:0;top:88px;width:1200px">Sectors</h2>

  <div class="abs card" style="left:90px;top:195px">
    <div class="photo" role="img" aria-label="Hands passing a small model house and keys" style="background:linear-gradient(135deg,#2c3a5a,#b88a5e 60%,#e9e4dd)"></div>
    <span class="tag">Real Estate</span>
    <p>Lorem ipsum dolor sit met,consectetur adipiscing elit, sed do eiusmod empor incididunt ut labore et dolore</p>
    <span class="more">Read More</span>
  </div>
  <div class="abs card" style="left:435px;top:195px">
    <div class="photo" role="img" aria-label="Laptop and phone showing an online store" style="background:linear-gradient(135deg,#3a3a3a,#d8dde6 55%,#6b6f77)"></div>
    <span class="tag">E-Commerce</span>
    <p>Lorem ipsum dolor sit met,consectetur adipiscing elit, sed do eiusmod empor incididunt ut labore et dolore</p>
    <span class="more">Read More</span>
  </div>
  <div class="abs card" style="left:782px;top:195px">
    <div class="photo" role="img" aria-label="Doctor holding hands with an elderly patient" style="background:linear-gradient(135deg,#dfe3e6,#c7b9a8 60%,#b07a3a)"></div>
    <span class="tag">Healthcare</span>
    <p>Lorem ipsum dolor sit met,consectetur adipiscing elit, sed do eiusmod empor incididunt ut labore et dolore</p>
    <span class="more">Read More</span>
  </div>

  <div class="abs card" style="left:90px;top:651px">
    <div class="photo" role="img" aria-label="Hands receiving lotion from a pump bottle" style="background:linear-gradient(135deg,#e9ecef,#dcd2cb 60%,#f3f3f3)"></div>
    <span class="tag">Beauty &amp; Personal Care</span>
    <p>Lorem ipsum dolor sit met,consectetur adipiscing elit, sed do eiusmod empor incididunt ut labore et dolore</p>
    <span class="more">Read More</span>
  </div>
  <div class="abs card" style="left:435px;top:651px">
    <div class="photo" role="img" aria-label="Team working on laptops and tablets around a desk" style="background:linear-gradient(135deg,#6b6b66,#a9a59c 55%,#4a4a48)"></div>
    <span class="tag">Technology</span>
    <p>Lorem ipsum dolor sit met,consectetur adipiscing elit, sed do eiusmod empor incididunt ut labore et dolore</p>
    <span class="more">Read More</span>
  </div>
  <div class="abs card" style="left:782px;top:651px">
    <div class="photo" role="img" aria-label="Mining site lit up at night" style="background:linear-gradient(180deg,#0e1a4a,#1d2c63 60%,#3a3a40)"></div>
    <span class="tag">Resources</span>
    <p>Lorem ipsum dolor sit met,consectetur adipiscing elit, sed do eiusmod empor incididunt ut labore et dolore</p>
    <span class="more">Read More</span>
  </div>
</section>

<!-- global outlook -->
<div class="abs" style="left:0;top:2519px;width:316px;height:583px;background:var(--purple)"></div>
<div class="abs photo" role="img" aria-label="Financial chart lines rising over stacked coins" style="left:0;top:2606px;width:587px;height:408px;background:linear-gradient(135deg,#d7b58a 0%,#6f8fa8 40%,#1f4f78 75%,#0f2d4d 100%)"></div>
<div class="abs outlook-text">
  <h2 class="left-title">Global Outlook</h2>
  <p>Lorem ipsum dolor sit amet, consectetur adipiscing elit, sed do eiusmod tempor incididunt ut labore et dolore magna aliqua. Ut enim ad minim veniam, quis nostrud exercitation ullamco laboris nisi ut aliquip ex ea commodo consequat. Duis aute irure dolor in reprehenderit in voluptate velit esse cillum dolore eu fugiat nulla pariatur. Excepteur sint occaecat cupidatat non proident, sunt in culpa qui officia deserunt mollit anim id est laborum</p>
  <span class="btn">Read More</span>
</div>

<!-- media -->
<h2 class="abs section-title" style="left:0;top:3188px;width:1200px">Media</h2>
<svg width="0" height="0" style="position:absolute"><defs><symbol id="arrow" viewBox="0 0 18 10"><path d="M0 5h15M11 1l5 4-5 4" fill="none" stroke="#886aae" stroke-width="2"/></symbol></defs></svg>

<article class="abs post" style="left:100px;top:3293px;width:487px;height:603px">
  <div class="photo" role="img" aria-label="Person using a calculator beside a laptop and paperwork" style="width:487px;height:371px;background:linear-gradient(135deg,#2f3a46,#c9d3dc 50%,#eef2f5)"></div>
  <div style="padding:22px 20px 0">
    <h3>Lorem ipsum dolor sit amet, adipiscing elit, sed do eiusmod tempor</h3>
    <p style="margin-top:14px;text-align:justify">Lorem ipsum dolor sit amet, consectetur adipiscing elit, sed do eiusmod tempor incididunt ut labore et dolore magna aliqua. Quis ipsum suspendisse ultrices gravida.</p>
    <span class="more" style="margin-top:14px">Read More <svg width="18" height="10"><use href="#arrow"/></svg></span>
  </div>
</article>

<article class="abs post mini" style="left:613px;top:3293px">
  <div class="body" style="left:22px">
    <h3>Lorem ipsum dolor sit amet, consectetur adipiscing</h3>
    <p>Lorem ipsum dolor sit amet, consectetur adipiscing elit, sed do eiusmod</p>
    <span class="more">Read More <svg width="18" height="10"><use href="#arrow"/></svg></span>
  </div>
  <div class="photo" role="img" aria-label="Hand placing a coin on stacks of coins" style="left:331px;background:linear-gradient(135deg,#f2f0ec,#c8b79a 60%,#6f5a3c)"></div>
</article>

<article class="abs post mini" style="left:613px;top:3502px">
  <div class="photo" role="img" aria-label="Parent and child reading together" style="left:0;background:linear-gradient(135deg,#6b7d8c,#d9a98a 55%,#c4c9cc)"></div>
  <div class="body" style="left:184px">
    <h3>Lorem ipsum dolor sit amet, consectetur adipiscing</h3>
    <p>Lorem ipsum dolor sit amet, consectetur adipiscing elit, sed do eiusmod</p>
    <span class="more">Read More <svg width="18" height="10"><use href="#arrow"/></svg></span>
  </div>
</article>

<article class="abs post mini" style="left:613px;top:3711px">
  <div class="body" style="left:22px">
    <h3>Lorem ipsum dolor sit amet, consectetur adipiscing</h3>
    <p>Lorem ipsum dolor sit amet, consectetur adipiscing elit, sed do eiusmod</p>
    <span class="more">Read More <svg width="18" height="10"><use href="#arrow"/></svg></span>
  </div>
  <div class="photo" role="img" aria-label="Blue financial growth chart with rising arrow" style="left:331px;background:linear-gradient(135deg,#cfe3f5,#3f86c9 55%,#e8f1fa)"></div>
</article>

<!-- contact -->
<div class="abs footer-bg"></div>
<section class="abs contact">
  <h2 class="section-title">Contact Us</h2>
  <div class="field" style="left:68px;top:160px;width:437px;height:50px">&#9679; First Name</div>
  <div class="field" style="left:515px;top:160px;width:417px;height:50px">&#9679; Last Name</div>
  <div class="field" style="left:68px;top:222px;width:864px;height:51px">&#9742; Your phone</div>
  <div class="field" style="left:68px;top:286px;width:864px;height:49px">&#9993; Your Email</div>
  <div class="field area" style="left:68px;top:347px;width:864px;height:133px">&#9679; How Can we help you?</div>
  <div class="abs submit">Submit</div>
</section>

<!-- footer -->
<footer>
  <div class="abs brand foot-brand">Meridale Holding<br>Partners</div>
  <div class="abs socials" aria-label="Social links"><span></span><span></span><span></span><span></span><span></span></div>

  <h4 class="abs foot-h" style="left:449px;top:4692px">Links</h4>
  <ul class="abs foot-list" style="left:451px;top:4758px"><li>Home</li><li>About Us</li><li>Expertise</li><li>Global Outlook</li></ul>
  <ul class="abs foot-list" style="left:720px;top:4758px"><li>Sectors</li><li>Management</li><li>Media</li><li>Contact Us</li></ul>

  <h4 class="abs foot-h" style="left:1005px;top:4692px">Important</h4>
  <ul class="abs foot-list" style="left:1006px;top:4758px"><li>Sign In</li><li>FAQ</li><li>Career</li></ul>

  <p class="abs copy">Copyright &copy; 2021 | Meridale Holding Partners | All rights reserved.</p>
</footer>

</body>
</html>
```